Name of company is Bluebird Meadow Shear Sharpening and Sales.Card design basic idea; I'm thinking back side just showing a sharp BLUEBIRD MEADOW. Front side: I'm thinking a tiger showing teeth and claws.With the words "Bluebird Meadow" larger type emphasized on one line.Then "Shear Sharpening and Sales" on the next line.Other info on front of card should be my name and phone #'s and address: Marcus Pellingham P (407)555-0174 CP (321)555-0138 My address is NOT to be emphasized.Can go at bottom of card. It is: 5127 Brennigan Lane Orlando FL 32899 If all that's too much to fit without looking cluttered than maybe the claw on the front with all the contact info. and just the Tiger on back of card. Whichever looks best.

Target Market(s)

Beauty Salons

Industry/Entity Type

It Company

Contact Information for Business Card

The 2 images,the claw and the tiger,could be either illustrations or photos.Whatever looks best.Got to be eye grabbing either way.

Requirements
Must have
• Contact info. Must be in color. And emphasize the identity. BLUEBIRD MEADOW.Tiger on one side.Showing TEETH. Bluebird Meadow on the other side. Showing the CLAW. .Both pics must emphasize SHARPNESS...This is a shear SHARPENING business. If one of the claw pics shows cutting grooves into something that's fine too. Card must show sharpness of the claw blade somehow.
Nice to have
• Attention grabbing. Images should jump off the card!
Should not have
• No boring cuddly tiger pics showing no teeth or claws or dull teeth or claws. No Black and whites.. No extra words other than what I've listed.

```html
<!DOCTYPE html>
<html lang="en">
<head>
<meta charset="utf-8">
<title>Bluebird Meadow Shear Sharpening and Sales – Business Card</title>
<link rel="stylesheet" href="https://fonts.googleapis.com/css2?family=Poppins:wght@400;500;600;700&display=swap">
<style>
  :root {
    --brand-blue: #3a55a6;
    --brand-blue-deep: #2f4896;
    --paper: #ffffff;
    --stage: #e9eaee;
    --tiger-orange: #d98a3c;
    --tiger-dark: #2a1d14;
    --tiger-light: #f2dcc0;
  }
  * { box-sizing: border-box; margin: 0; padding: 0; }
  html, body {
    width: 1200px; height: 900px; overflow: hidden;
    background: var(--stage);
    font-family: "Poppins", sans-serif;
  }
  .stage {
    width: 1200px; height: 900px;
    display: flex; flex-direction: column; align-items: center; justify-content: center;
    gap: 34px;
  }
  .card {
    position: relative; width: 700px; height: 400px; overflow: hidden;
    box-shadow: 0 10px 28px rgba(0,0,0,.22);
  }

  /* ---------- Back side ---------- */
  .card-back { background: var(--brand-blue); }
  .card-back .identity {
    position: absolute; left: 52px; top: 226px; color: var(--paper);
  }
  .identity-name {
    font-weight: 600; font-size: 32px; letter-spacing: 2px; line-height: 1;
  }
  .identity-tagline {
    margin-top: 6px; font-size: 12.5px; letter-spacing: 1.6px; font-weight: 400;
  }
  .claw-marks {
    position: absolute; left: 400px; top: 40px; width: 260px; height: 310px;
  }

  /* ---------- Front side ---------- */
  .card-front { background: var(--paper); }
  .front-panel {
    position: absolute; inset: 0;
    background: var(--brand-blue);
    clip-path: polygon(0 0, 350px 0, 376px 400px, 0 400px);
  }
  .name-band {
    position: absolute; left: 0; top: 58px; width: 372px; height: 62px;
    background: var(--paper);
    clip-path: polygon(0 0, 365px 0, 372px 62px, 0 62px);
    padding: 6px 0 0 54px; color: var(--brand-blue);
  }
  .name-band .identity-name { font-size: 25px; letter-spacing: 1.5px; }
  .name-band .identity-tagline { margin-top: 3px; font-size: 10px; letter-spacing: 1.2px; }
  .band-rule {
    position: absolute; left: 0; top: 128px; width: 374px; height: 3px; background: var(--paper);
  }
  .tiger-photo {
    position: absolute; left: 350px; top: 0; width: 350px; height: 400px;
    background:
      radial-gradient(ellipse at 50% 45%, var(--tiger-light) 0%, transparent 35%),
      linear-gradient(160deg, var(--tiger-orange) 0%, #c0702a 45%, var(--tiger-dark) 100%);
    clip-path: polygon(18px 40px, 330px 40px, 330px 400px, 32px 400px);
  }
  .person {
    position: absolute; left: 78px; top: 160px; color: var(--paper);
  }
  .person-name { font-size: 17px; font-weight: 500; letter-spacing: 2px; line-height: 1.2; }
  .person-role { font-size: 16px; font-weight: 500; letter-spacing: 1px; }
  .contact-list {
    position: absolute; left: 62px; top: 236px; list-style: none; color: var(--paper);
    font-size: 13.5px; letter-spacing: 1.2px; line-height: 1.45;
  }
  .contact-list li { display: flex; align-items: flex-start; gap: 10px; }
  .contact-list svg { width: 12px; height: 12px; margin-top: 4px; flex: none; }
  .contact-address { line-height: 1.3; }
  .hazard-stripes {
    position: absolute; left: 0; bottom: 14px; width: 378px; height: 18px;
    background: repeating-linear-gradient(115deg, var(--paper) 0 14px, transparent 14px 30px);
  }
</style>
</head>
<body>
<main class="stage">

  <section class="card card-back" aria-label="Card back">
    <div class="identity">
      <p class="identity-name">BLUEBIRD MEADOW</p>
      <p class="identity-tagline">Shear Sharpening and Sales</p>
    </div>
    <div class="claw-marks" role="img" aria-label="Four white claw slash marks tearing diagonally across the card"
         style="background: linear-gradient(135deg, rgba(255,255,255,.0) 0%, rgba(255,255,255,.35) 50%, rgba(255,255,255,.0) 100%);"></div>
  </section>

  <section class="card card-front" aria-label="Card front">
    <div class="front-panel"></div>
    <div class="tiger-photo" role="img" aria-label="Photograph of a snarling tiger showing sharp teeth"></div>
    <div class="name-band">
      <p class="identity-name">BLUEBIRD MEADOW</p>
      <p class="identity-tagline">Shear Sharpening and Sales</p>
    </div>
    <div class="band-rule"></div>

    <div class="person">
      <p class="person-name">MARCUS PELLINGHAM</p>
      <p class="person-role">Founder</p>
    </div>

    <ul class="contact-list">
      <li>
        <svg viewBox="0 0 24 24" fill="currentColor" aria-hidden="true"><path d="M6.6 10.8a15 15 0 0 0 6.6 6.6l2.2-2.2a1 1 0 0 1 1-.25 11.4 11.4 0 0 0 3.6.57 1 1 0 0 1 1 1V20a1 1 0 0 1-1 1A17 17 0 0 1 3 4a1 1 0 0 1 1-1h3.5a1 1 0 0 1 1 1c0 1.25.2 2.45.57 3.57a1 1 0 0 1-.25 1z"/></svg>
        <span>(407)555-0174</span>
      </li>
      <li>
        <svg viewBox="0 0 24 24" fill="none" stroke="currentColor" stroke-width="2.2" aria-hidden="true"><rect x="6" y="2" width="12" height="20" rx="2"/><line x1="11" y1="18" x2="13" y2="18"/></svg>
        <span>(321)555-0138</span>
      </li>
      <li>
        <svg viewBox="0 0 24 24" fill="currentColor" aria-hidden="true"><path d="M12 2a7 7 0 0 0-7 7c0 5 7 13 7 13s7-8 7-13a7 7 0 0 0-7-7zm0 9.5A2.5 2.5 0 1 1 12 6.5a2.5 2.5 0 0 1 0 5z"/></svg>
        <span class="contact-address">5127 Brennigan Lane<br>Orlando FL 32899</span>
      </li>
    </ul>

    <div class="hazard-stripes"></div>
  </section>

</main>
</body>
</html>
```